DEAN COLLOPY PROPERTY SERVICES

I want a business card that is clean and simple.
'Dean Collopy Property Services' is the title.
Somewhere on the card needs to be 'Carpentry, Tiling, painting and garden services'

On the back of card
PH 087 394 1526
email: deancollopypropertyservices@bluefinchmail.net

I have attached a picture of my other business. I would like the font and design to be similar to the bathroom business.

Many thanks.

```html
<!DOCTYPE html>
<html lang="en">
<head>
<meta charset="utf-8">
<title>Dean Collopy Property Services – Business Card</title>
<link rel="stylesheet" href="https://fonts.googleapis.com/css2?family=Montserrat:wght@400;500&display=swap">
<style>
  :root {
    --backdrop: #222222;
    --card-white: #ffffff;
    --ink: #111111;
    --band: #000000;
    --muted: #3a3a3a;
  }
  * { box-sizing: border-box; margin: 0; padding: 0; }
  html, body {
    width: 1200px;
    height: 780px;
    overflow: hidden;
    background: var(--backdrop);
    font-family: "Montserrat", sans-serif;
  }
  .stage {
    width: 1200px;
    height: 780px;
    display: flex;
    align-items: center;
    justify-content: center;
    gap: 40px;
  }
  .card {
    position: relative;
    width: 540px;
    height: 309px;
    background: var(--card-white);
    overflow: hidden;
    box-shadow: 0 10px 30px rgba(0,0,0,0.45);
  }

  /* Wordmark */
  .wordmark {
    display: flex;
    flex-direction: column;
    align-items: center;
    color: var(--ink);
  }
  .wordmark-name {
    font-size: 38px;
    font-weight: 500;
    letter-spacing: 0.5px;
    line-height: 1;
  }
  .wordmark-tag {
    margin-top: 6px;
    font-size: 11px;
    font-weight: 400;
    letter-spacing: 3.2px;
    line-height: 1;
  }
  .wordmark--light { color: var(--card-white); }

  /* Front */
  .card-front .wordmark {
    position: absolute;
    top: 84px;
    left: 0;
    right: 0;
  }
  .services {
    position: absolute;
    left: 0;
    right: 0;
    bottom: 52px;
    display: flex;
    justify-content: center;
    align-items: center;
    list-style: none;
    font-size: 14px;
    font-weight: 400;
    letter-spacing: 1px;
    color: var(--ink);
  }
  .services li + li {
    border-left: 1px solid var(--ink);
    margin-left: 8px;
    padding-left: 8px;
  }
  .services li { line-height: 22px; }

  /* Back */
  .band {
    position: absolute;
    top: 0;
    left: 0;
    right: 0;
    height: 140px;
    background: var(--band);
    display: flex;
    align-items: center;
    justify-content: center;
  }
  .band .wordmark { margin-top: 30px; }
  .contact {
    position: absolute;
    top: 158px;
    left: 0;
    right: 0;
    display: flex;
    flex-direction: column;
    align-items: center;
    color: var(--ink);
  }
  .contact-icons {
    display: flex;
    gap: 6px;
    margin-bottom: 14px;
  }
  .contact-icons svg { width: 20px; height: 20px; display: block; }
  .contact-phone {
    font-size: 16px;
    letter-spacing: 0.5px;
    margin-bottom: 20px;
  }
  .contact-email {
    font-size: 15px;
    letter-spacing: 0.3px;
  }
</style>
</head>
<body>
<main class="stage">

  <section class="card card-front" aria-label="Card front">
    <div class="wordmark">
      <span class="wordmark-name">Dean Collopy</span>
      <span class="wordmark-tag">PROPERTY SERVICES</span>
    </div>
    <ul class="services">
      <li>CARPENTRY</li>
      <li>TILING</li>
      <li>PAINTING</li>
      <li>GARDEN SERVICES</li>
    </ul>
  </section>

  <section class="card card-back" aria-label="Card back">
    <div class="band">
      <div class="wordmark wordmark--light">
        <span class="wordmark-name">Dean Collopy</span>
        <span class="wordmark-tag">PROPERTY SERVICES</span>
      </div>
    </div>
    <div class="contact">
      <div class="contact-icons">
        <svg viewBox="0 0 20 20" aria-label="Phone">
          <circle cx="10" cy="10" r="10" fill="#000"/>
          <path d="M7 5.5c.4-.3.9-.2 1.1.2l.8 1.6c.2.4.1.8-.2 1l-.6.5c.4 1 1.3 1.9 2.3 2.3l.5-.6c.3-.3.7-.4 1-.2l1.6.8c.4.2.5.7.2 1.1l-.6.8c-.4.5-1.1.7-1.7.4-2.2-.9-4-2.7-4.9-4.9-.3-.6-.1-1.3.4-1.7z" fill="#fff"/>
        </svg>
        <svg viewBox="0 0 20 20" aria-label="Email">
          <circle cx="10" cy="10" r="10" fill="#000"/>
          <rect x="5" y="6.5" width="10" height="7" rx="0.8" fill="none" stroke="#fff" stroke-width="1.2"/>
          <path d="M5.4 7l4.6 3.6L14.6 7" fill="none" stroke="#fff" stroke-width="1.2"/>
        </svg>
      </div>
      <p class="contact-phone">087 394 1526</p>
      <p class="contact-email">deancollopypropertyservices@bluefinchmail.net</p>
    </div>
  </section>

</main>
</body>
</html>
```